Flash Banner Ad for web advertising

We are a float centre in Auckland, New Zealand. Please see our website at www.calmtidepod.co.nz for more info on us and what we provide

We need an HTML5 flash ad for various websites promoting our product that generates traffic onto our website.

Dimensions (W x H): 300x250 pixels
Max File Size: 80 kB
Format: HTML5

This banner needs to be brief (3-4 slides) and visual, with booking being the last slide. Should say that the product provides relaxation and other benefits as can be seen on home page of our site. Needs to be a summary as people do not look at banners for long.

Please use images attached or images from our site, please message if you need more resources:
https://www.filecrate.example/sh/qt7bn2lw4kxd/ZZRmLopq8vHs2TnBa?dl=0

Target Market(s)

Stressed individuals who need a break from every day life.

Industry/Entity Type

Health And Wellness

Colors
3176b5
0592cd
34a7d8
add136
9bcb3c
33b8a4
ffffff

Requirements
Must have
• Slides that finish into a website book now link

```html
<!DOCTYPE html>
<html lang="en">
<head>
<meta charset="utf-8">
<title>Calmtide Pod – Banner Slides</title>
<link href="https://fonts.googleapis.com/css2?family=Quicksand:wght@400;500;600&display=swap" rel="stylesheet">
<style>
  :root {
    --brand-blue: #3176b5;
    --brand-sky: #34a7d8;
    --lime: #add136;
    --lime-deep: #9bcb3c;
    --white: #ffffff;
    --night: #0b0f1c;
    --page: #ffffff;
  }
  * { box-sizing: border-box; margin: 0; padding: 0; }
  html, body { width: 1200px; height: 992px; overflow: hidden; background: var(--page); }
  body { position: relative; font-family: "Quicksand", sans-serif; color: var(--white); }

  .slide {
    position: absolute;
    width: 480px;
    height: 400px;
    overflow: hidden;
    border: 1.5px solid #1a1a1a;
  }
  .slide--intro    { left: 91px;  top: 59px;  background: var(--brand-blue); }
  .slide--relax    { left: 638px; top: 59px; }
  .slide--discover { left: 91px;  top: 514px; }
  .slide--book     { left: 638px; top: 514px; }

  .photo { position: absolute; inset: 0; }
  .photo--relax {
    background:
      radial-gradient(ellipse 55% 40% at 62% 45%, #6c5a55 0%, rgba(60,50,60,0.5) 45%, transparent 75%),
      linear-gradient(180deg, #0c0d14 0%, #10162c 50%, #123a8a 78%, #1c50c0 100%);
  }
  .photo--discover {
    background:
      radial-gradient(ellipse 60% 35% at 50% 30%, #c9def0 0%, #7ea7cf 40%, transparent 75%),
      radial-gradient(ellipse 70% 45% at 50% 85%, #3b67a8 0%, #16284a 60%, transparent 90%),
      linear-gradient(180deg, #05070d 0%, #0a1426 100%);
  }
  .photo--book {
    background:
      radial-gradient(circle at 76% 62%, #f2a34a 0%, rgba(230,120,60,0.4) 12%, transparent 30%),
      linear-gradient(90deg, #1a2fd0 0%, #2c4df0 22%, #3fa3a8 42%, #e8e4dc 55%, #f4eee6 75%, #c45a2e 88%, #e7e2da 100%);
  }

  /* brand lockup */
  .brand { display: flex; align-items: center; gap: 14px; }
  .brand__mark {
    width: 62px; height: 62px; border-radius: 50%;
    border: 3px solid var(--white);
    flex: none;
  }
  .brand__name { font-size: 44px; font-weight: 400; color: var(--white); line-height: 1; letter-spacing: 1px; white-space: nowrap; }
  .brand__sub  { display: block; font-size: 12px; letter-spacing: 3px; margin-top: 6px; text-transform: uppercase; }

  .slide--intro .brand { position: absolute; left: 70px; top: 34px; }
  .divider {
    position: absolute; left: 34px; right: 34px; top: 162px;
    border-top: 2px dashed rgba(255,255,255,0.75);
  }
  .intro-copy {
    position: absolute; left: 8px; right: 8px; top: 190px;
    font-size: 23.5px; line-height: 32px; text-align: center; font-weight: 500;
    white-space: nowrap;
  }

  /* arrow tags */
  .tag {
    position: absolute;
    height: 46px;
    padding: 0 30px 0 22px;
    display: flex; align-items: center;
    font-size: 26px; font-weight: 500; line-height: 1;
    white-space: nowrap;
    background: var(--lime);
    color: var(--white);
    clip-path: polygon(0 0, calc(100% - 18px) 0, 100% 50%, calc(100% - 18px) 100%, 0 100%);
  }
  .tag--right-end {
    padding: 0 22px 0 36px;
    justify-content: center;
    clip-path: polygon(18px 0, 100% 0, 100% 100%, 18px 100%, 0 50%);
  }
  .slide--relax .tag               { left: 0; top: 19px; width: 270px; }
  .slide--discover .tag--top       { left: 0; top: 19px; width: 272px; }
  .slide--discover .tag--right-end { right: 0; bottom: 14px; width: 262px; }
  .slide--book .tag                { left: 0; top: 16px; width: 258px; }

  /* booking band */
  .book-band {
    position: absolute; left: 0; right: 0; bottom: 0; height: 94px;
    background: var(--brand-blue);
    display: flex; align-items: center; justify-content: space-between;
    padding: 0 22px 0 14px;
  }
  .book-band .brand__mark { width: 56px; height: 56px; }
  .book-band .brand__name { font-size: 38px; }
  .book-band .brand__sub  { font-size: 10px; }
  .book-button {
    width: 157px; height: 53px; border-radius: 27px;
    background: var(--lime-deep);
    color: var(--white);
    font-family: inherit; font-size: 26px; font-weight: 500;
    white-space: nowrap;
    display: flex; align-items: center; justify-content: center;
    text-decoration: none;
  }
</style>
</head>
<body>

  <section class="slide slide--intro">
    <div class="brand">
      <span class="brand__mark"></span>
      <span class="brand__name">calmtide<span class="brand__sub">Float Centre</span></span>
    </div>
    <div class="divider"></div>
    <p class="intro-copy">We Achieve relief from pain,<br>alleviate stress, experience complete<br>mindfulness and stillness. Discover a<br>once in a lifetime experience that<br>some describe as a complete rebirth<br>and purification of body and mind</p>
  </section>

  <section class="slide slide--relax">
    <div class="photo photo--relax" role="img" aria-label="Woman floating with eyes closed in dark blue-lit water"></div>
    <span class="tag">Deep Relaxation</span>
  </section>

  <section class="slide slide--discover">
    <div class="photo photo--discover" role="img" aria-label="Man climbing into an open float pod lit in blue"></div>
    <span class="tag tag--top">Self-Discovery</span>
    <span class="tag tag--right-end">Stress Relief</span>
  </section>

  <section class="slide slide--book">
    <div class="photo photo--book" role="img" aria-label="Float room with a blue-lit pod door, towel shelves and a salt lamp"></div>
    <span class="tag">Relieves Pain</span>
    <div class="book-band">
      <div class="brand">
        <span class="brand__mark"></span>
        <span class="brand__name">calmtide<span class="brand__sub">Float Centre</span></span>
      </div>
      <a class="book-button" href="https://www.calmtidepod.co.nz">Book now</a>
    </div>
  </section>

</body>
</html>
```